Improvement of design for elearning template

Our company provides web based elearning courses for employees. We have a design layout for the different slides which can be found here: https://www.filecrate-share.com/sh/qemvirt7xnoa2lup/KLpQzRtYwMbDfHsnVcEkGaUoPi?dl=0. The content will be added later. At this point we are just looking for a design layout that works with different content types like images, text, quiz & videos. What we would ask you, is to pick randomly 1 or 2 of the elearning slides from the existing designs and suggest improvements or come up with an alternative design. The winner of the design project can work on all slides and this will be a project with a much larger budget.
Target Market(s)
Employees in large enterprises
Look and feel
Each slider illustrates characteristics of the customer's brand and the style your logo design should communicate.

```html
<!DOCTYPE html>
<html lang="en">
<head>
<meta charset="utf-8">
<title>Lesson 2 – What is Lorem Ipsum?</title>
<link rel="stylesheet" href="https://fonts.googleapis.com/css2?family=Poppins:wght@300;400;500;600&display=swap">
<style>
  :root {
    --page-bg: #dde7fa;
    --card-bg: #ffffff;
    --brand-blue: #2f60b1;
    --deep-blue: #1f3f8f;
    --body-text: #3b3b48;
    --strong-text: #25252f;
    --track: #ffffff;
    --art-light: #b7cdf5;
    --art-mid: #7fa3ea;
    --art-dark: #3c6bcf;
  }
  * { box-sizing: border-box; margin: 0; padding: 0; }
  html, body { width: 1200px; height: 619px; overflow: hidden; }
  body {
    position: relative;
    background: var(--page-bg);
    font-family: "Poppins", sans-serif;
    color: var(--body-text);
  }
  .brand {
    position: absolute; left: 22px; top: 16px;
    display: flex; align-items: center; gap: 10px;
  }
  .brand-dot {
    width: 30px; height: 30px; border-radius: 50%;
    border: 2.5px solid var(--brand-blue);
  }
  .brand-name {
    font-size: 23px; font-weight: 400; color: var(--brand-blue);
    letter-spacing: 0.2px;
  }
  .home-button {
    position: absolute; left: 1075px; top: 20px;
    width: 74px; height: 28px; border-radius: 14px;
    background: var(--brand-blue); color: #fff;
    font-size: 16px; font-weight: 500;
    display: flex; align-items: center; justify-content: center;
    text-decoration: none;
  }
  .card-frame {
    position: absolute; left: 99px; top: 63px; width: 1002px; height: 493px;
    border: 2px solid #ffffff; border-radius: 46px;
  }
  .card {
    position: absolute; left: 113px; top: 77px; width: 974px; height: 465px;
    background: var(--card-bg); border-radius: 38px;
  }
  .lesson-title {
    position: absolute; left: 146px; top: 119px;
    font-size: 27px; font-weight: 600; color: var(--brand-blue);
    line-height: 1.2;
  }
  .title-rule {
    position: absolute; left: 148px; top: 154px;
    width: 106px; height: 3px; background: var(--brand-blue);
  }
  .intro {
    position: absolute; left: 144px; top: 169px; width: 920px;
    font-size: 17px; font-weight: 300; line-height: 20.5px;
  }
  .key-points {
    position: absolute; left: 199px; top: 252px; width: 370px;
    list-style: none;
    font-size: 19.5px; font-weight: 500; color: var(--strong-text);
    line-height: 25.6px;
  }
  .key-points li { position: relative; margin-bottom: 12px; }
  .key-points li::before {
    content: ""; position: absolute; left: -16px; top: 11px;
    width: 6px; height: 6px; border-radius: 50%; background: var(--strong-text);
  }
  .history {
    position: absolute; left: 144px; top: 401px; width: 430px;
    font-size: 17px; font-weight: 300; line-height: 20.5px;
  }
  .lesson-art {
    position: absolute; left: 575px; top: 234px; width: 604px; height: 342px;
    border-radius: 170px 40px 30px 170px;
    background: linear-gradient(135deg, var(--art-light) 0%, var(--art-mid) 55%, var(--art-dark) 100%);
    opacity: 0.85;
  }
  .progress {
    position: absolute; left: 56px; top: 566px;
    display: flex; align-items: center;
  }
  .progress-track {
    position: relative; width: 335px; height: 8px;
    background: repeating-linear-gradient(90deg, var(--track) 0 16px, #cfdcf5 16px 17px);
    border-radius: 4px;
  }
  .progress-fill {
    position: absolute; left: 0; top: 0; width: 172px; height: 8px;
    background: var(--brand-blue); border-radius: 4px 0 0 4px;
  }
  .progress-knob {
    position: absolute; left: 0; top: -3px;
    width: 14px; height: 14px; border-radius: 50%; background: var(--brand-blue);
  }
  .progress-label {
    margin-left: 24px;
    font-size: 17.5px; font-weight: 500; color: var(--brand-blue);
  }
  .progress-label .sep { margin: 0 12px; }
</style>
</head>
<body>
  <header>
    <div class="brand">
      <span class="brand-dot"></span>
      <span class="brand-name">COMPANY NAME</span>
    </div>
    <a class="home-button" href="#">Home</a>
  </header>

  <div class="card-frame"></div>
  <main class="card"></main>

  <h1 class="lesson-title">What is Lorem Ipsum?</h1>
  <div class="title-rule"></div>

  <p class="intro">Lorem Ipsum is simply dummy text of the printing and typesetting industry. Lorem Ipsum has been the industry's standard dummy text ever since the 1500s, when an unknown printer took a galley of type and scrambled it to make a type specimen book.</p>

  <ul class="key-points">
    <li>It has survived not only five centuries,</li>
    <li>but also the leap into electronic typesetting, remaining essentially unchanged.</li>
  </ul>

  <p class="history">It was popularised in the 1960s with the release of Tiposet sheets containing Lorem Ipsum passages, and more recently with desktop publishing software like Quillon PageForge including versions of Lorem Ipsum.</p>

  <div class="lesson-art" role="img" aria-label="Illustration of a large desktop monitor showing a presenter and documents, with a globe, paper plane, wifi symbol and a person working on a laptop while sitting on a stack of books"></div>

  <footer class="progress">
    <div class="progress-track">
      <div class="progress-fill"></div>
      <div class="progress-knob"></div>
    </div>
    <div class="progress-label">Overall Progress 30%<span class="sep">•</span>Lesson 2</div>
  </footer>
</body>
</html>
```